New Signage Design Project

Real estate company looking for signage, PowerPoint and stationery branding. Signs will be placed in front of homes and other properties being sold

Name of company is Tern Haven, LLC

Requirements
Must have
• Name of company - Tern Haven, LLC

```html
<!DOCTYPE html>
<html lang="en">
<head>
<meta charset="utf-8">
<title>Tern Haven, LLC — Business Card Front and Back</title>
<link rel="stylesheet" href="https://fonts.googleapis.com/css2?family=Roboto:wght@300;500&family=Roboto+Condensed:wght@700&display=swap">
<style>
  :root {
    --sheet: #bdbdbd;
    --ink-dark: #212d2e;
    --sage: #82a4a4;
    --coral: #e4525e;
    --paper: #ffffff;
    --caption: #2b2f30;
  }
  html, body {
    margin: 0;
    padding: 0;
    overflow: hidden;
  }
  .sheet {
    position: relative;
    width: 1028px;
    height: 1200px;
    background: var(--sheet);
    overflow: hidden;
  }
  .sheet-title {
    position: absolute;
    top: 19px;
    left: 0;
    width: 100%;
    margin: 0;
    text-align: center;
    font-family: "Roboto Condensed", sans-serif;
    font-weight: 700;
    font-size: 14px;
    letter-spacing: 0.2px;
    color: var(--caption);
  }
  .card {
    position: absolute;
    left: 37px;
    width: 955px;
    height: 545px;
    overflow: hidden;
  }
  /* Front */
  .card-front {
    top: 55px;
    background: var(--ink-dark);
  }
  .band {
    position: absolute;
    left: 0;
    width: 100%;
    height: 83px;
    background: var(--sage);
  }
  .band-top { top: 0; }
  .band-bottom { bottom: 0; }
  .front-brand {
    position: absolute;
    top: 83px;
    left: 0;
    width: 100%;
    height: 379px;
    display: flex;
    align-items: center;
    justify-content: center;
    gap: 22px;
  }
  .brand-dot {
    width: 54px;
    height: 54px;
    border-radius: 50%;
    background: var(--coral);
  }
  .brand-name {
    margin: 0;
    font-family: "Roboto", sans-serif;
    font-weight: 500;
    color: var(--sage);
    letter-spacing: 0.5px;
    text-transform: uppercase;
  }
  .front-brand .brand-name { font-size: 44px; }
  /* Back */
  .card-back {
    top: 623px;
    background: var(--ink-dark);
  }
  .skyline {
    position: absolute;
    top: 0;
    left: 0;
    width: 100%;
    height: 262px;
    background: linear-gradient(to bottom, var(--paper) 0%, var(--paper) 12%, #9aa6a6 45%, var(--ink-dark) 100%);
  }
  .back-brand {
    position: absolute;
    left: 37px;
    top: 300px;
    width: 300px;
    height: 240px;
    display: flex;
    align-items: center;
  }
  .back-brand .brand-name {
    font-size: 34px;
    color: var(--paper);
  }
  .contact-list {
    position: absolute;
    left: 370px;
    top: 308px;
    margin: 0;
    padding: 0;
    list-style: none;
  }
  .contact-item {
    position: absolute;
    left: 0;
    display: flex;
    align-items: center;
    white-space: nowrap;
    font-family: "Roboto", sans-serif;
    font-weight: 300;
    font-size: 26px;
    color: var(--paper);
  }
  .contact-item:nth-child(1) { top: 0; }
  .contact-item:nth-child(2) { top: 56px; }
  .contact-item:nth-child(3) { top: 121px; }
  .contact-item:nth-child(4) { top: 173px; }
  .contact-icon {
    width: 34px;
    height: 34px;
    margin-right: 32px;
    fill: var(--sage);
  }
</style>
</head>
<body>
<main class="sheet">
  <h1 class="sheet-title">BUSINESS CARD FRONT AND BACK/REVERSE</h1>

  <section class="card card-front" aria-label="Business card front">
    <div class="band band-top"></div>
    <div class="front-brand">
      <span class="brand-dot"></span>
      <p class="brand-name">Tern Haven, LLC</p>
    </div>
    <div class="band band-bottom"></div>
  </section>

  <section class="card card-back" aria-label="Business card back">
    <div class="skyline" role="img" aria-label="City skyline silhouette in dark slate against white"></div>

    <div class="back-brand">
      <p class="brand-name">Tern Haven, LLC</p>
    </div>

    <ul class="contact-list">
      <li class="contact-item">
        <svg class="contact-icon" viewBox="0 0 24 24" aria-hidden="true">
          <path d="M12 1.5c-4 0-7 3-7 7 0 5 7 14 7 14s7-9 7-14c0-4-3-7-7-7zm0 9.6a2.6 2.6 0 1 1 0-5.2 2.6 2.6 0 0 1 0 5.2z"/>
        </svg>
        ADDRESS
      </li>
      <li class="contact-item">
        <svg class="contact-icon" viewBox="0 0 24 24" aria-hidden="true">
          <path d="M6.6 10.8c1.4 2.8 3.8 5.2 6.6 6.6l2.2-2.2c.3-.3.7-.4 1-.2 1.1.4 2.3.6 3.6.6.6 0 1 .4 1 1V20c0 .6-.4 1-1 1C10.6 21 3 13.4 3 4c0-.6.4-1 1-1h3.5c.6 0 1 .4 1 1 0 1.3.2 2.5.6 3.6.1.3 0 .7-.2 1l-2.3 2.2z"/>
        </svg>
        PHONE
      </li>
      <li class="contact-item">
        <svg class="contact-icon" viewBox="0 0 24 24" aria-hidden="true">
          <path d="M12 2a10 10 0 1 0 0 20 10 10 0 0 0 0-20zm-1 2.1V7H8.3c.6-1.5 1.6-2.6 2.7-2.9zm2 0c1.1.3 2.1 1.4 2.7 2.9H13V4.1zM6.3 7H4.9a8 8 0 0 1 3-2.4c-.6.7-1.1 1.5-1.6 2.4zm11.4 0a8.6 8.6 0 0 0-1.6-2.4 8 8 0 0 1 3 2.4h-1.4zM4.2 9h2c-.1.6-.2 1.3-.2 2h-2c0-.7.1-1.4.2-2zm4 0H11v2H8c0-.7.1-1.4.2-2zM13 9h2.8c.1.6.2 1.3.2 2h-3V9zm4.8 0h2c.1.6.2 1.3.2 2h-2c0-.7-.1-1.4-.2-2zM4 13h2c0 .7.1 1.4.2 2h-2c-.1-.6-.2-1.3-.2-2zm4 0h3v2H8.2c-.1-.6-.2-1.3-.2-2zm5 0h3c0 .7-.1 1.4-.2 2H13v-2zm5 0h2c0 .7-.1 1.4-.2 2h-2c.1-.6.2-1.3.2-2zM4.9 17h1.4c.5.9 1 1.7 1.6 2.4a8 8 0 0 1-3-2.4zm3.4 0H11v2.9c-1.1-.3-2.1-1.4-2.7-2.9zm4.7 0h2.7c-.6 1.5-1.6 2.6-2.7 2.9V17zm4.7 0h1.4a8 8 0 0 1-3 2.4c.6-.7 1.1-1.5 1.6-2.4z"/>
        </svg>
        WEBSITE
      </li>
      <li class="contact-item">
        <svg class="contact-icon" viewBox="0 0 24 24" aria-hidden="true">
          <path d="M2 5h20v14H2V5zm2 2v.4l8 5.4 8-5.4V7H4zm0 2.8V17h4.6L4 9.8zm16 0L15.4 17H20V9.8zM10.6 17h2.8L12 15.1 10.6 17zm-.6-2.6 2 1.3 2-1.3-2 2.9-2-2.9z"/>
        </svg>
        EMAIL ADDRESS
      </li>
    </ul>
  </section>
</main>
</body>
</html>
```